Landing page for 'Page under construction' page

We need a simple landing page that we can use while our page is under construction.

The page should be made ready so that all we need to do is drop it on our web server and then it will function as our webpage. The domain is www.tlv.no

Please see attached file for instructions on what elements to include in the landing page. The Brand Book provides fonts and color palette.

Coding

Coded - Design and coding required

Number of Pages Required

1 page

Colors

Designer to choose colors to be used in the design.

```html
<!DOCTYPE html>
<html lang="en">
<head>
<meta charset="utf-8">
<title>Tellvera – Business value, faster</title>
<link href="https://fonts.googleapis.com/css2?family=Montserrat:wght@400;500;600;700;800&family=Open+Sans:wght@400;600&display=swap" rel="stylesheet">
<style>
:root{
  --navy:#0a1733;
  --navy-2:#12305f;
  --blue:#1d4f9a;
  --orange:#f2703a;
  --orange-2:#f59a5c;
  --ink:#222831;
  --muted:#5b6270;
  --line:#e6e8ec;
  --paper:#ffffff;
  --soft:#f6f7f9;
  --black:#0b0b0c;
}
*{box-sizing:border-box;margin:0;padding:0}
html,body{width:1200px;height:3540px;overflow:hidden}
body{font-family:"Open Sans",Arial,sans-serif;color:var(--ink);background:var(--paper);position:relative}
h1,h2,h3,h4,.brand,.btn,.nav{font-family:"Montserrat",Arial,sans-serif}
.abs{position:absolute}

/* header + hero */
.hero{position:absolute;left:0;top:0;width:1200px;height:760px;
  background:radial-gradient(ellipse at 70% 30%,#1b4f8f 0%,#0f2c57 35%,var(--navy) 75%);overflow:hidden}
.site-header{position:absolute;left:0;top:0;width:1200px;height:72px;display:flex;align-items:center;padding:0 50px;background:rgba(5,12,30,.55)}
.brand{font-weight:800;font-size:30px;color:#fff;letter-spacing:-.5px;display:flex;align-items:center;gap:8px}
.brand-dot{width:10px;height:10px;background:var(--orange)}
.nav{display:flex;gap:34px;margin-left:120px;font-size:11px;font-weight:600;color:#fff;letter-spacing:.5px}
.header-tools{margin-left:auto;display:flex;align-items:center;gap:16px}
.lang{border:1px solid #fff;color:#fff;font:600 11px "Montserrat",sans-serif;padding:5px 10px;border-radius:3px}
.search{width:28px;height:28px;border:1.5px solid var(--orange);border-radius:50%;display:flex;align-items:center;justify-content:center}
.btn{display:inline-block;font-weight:600;font-size:12px;letter-spacing:.4px;padding:10px 20px;border-radius:4px;text-transform:uppercase}
.btn-orange{background:var(--orange);color:#fff}
.btn-outline{border:1.5px solid #fff;color:#fff}
.btn-white{background:#fff;color:var(--orange)}
.hero-copy{position:absolute;left:60px;top:340px;width:520px;color:#fff}
.hero-copy h1{font-size:46px;font-weight:800;line-height:1.08;letter-spacing:.3px}
.hero-copy p{font-size:17px;line-height:1.45;margin:22px 0 34px;color:#e7eefb}
.hero-visual{position:absolute;left:640px;top:300px;width:560px;height:400px;border-radius:10px 0 0 10px;
  background:linear-gradient(135deg,#dfe6f1 0%,#f4f6fa 45%,#9fb1cb 100%)}

/* section titles */
.eyebrow{font:600 14px "Montserrat",sans-serif;color:var(--ink);text-align:center;letter-spacing:.5px}
.section-title{font:700 30px "Montserrat",sans-serif;color:var(--blue);text-align:center;margin-top:6px}
.title-rule{width:70px;height:3px;background:var(--orange);margin:14px auto 0}

/* about */
.about{position:absolute;left:0;top:760px;width:1200px;height:700px;background:var(--soft)}
.about .eyebrow{margin-top:60px}
.about-frame{position:absolute;left:165px;top:225px;width:360px;height:330px;border:3px solid var(--orange)}
.about-photo{position:absolute;left:140px;top:200px;width:360px;height:330px;background:linear-gradient(135deg,#1f3552,#5a708b 55%,#c9d2dd)}
.about-text{position:absolute;left:580px;top:215px;width:480px}
.about-text h3{font-size:20px;font-weight:700;color:var(--ink);padding-left:12px;border-left:4px solid var(--orange);margin-bottom:12px}
.about-text p{font-size:11.5px;line-height:1.6;color:var(--muted);margin-bottom:22px}

/* platform */
.platform{position:absolute;left:0;top:1470px;width:1200px;height:400px}
.platform .section-title{margin-top:40px}
.platform-sub{text-align:center;font-size:13px;color:var(--muted);margin-top:10px}
.feature{position:absolute;top:150px;display:flex;gap:14px;align-items:flex-start}
.feature h4{font-size:16px;font-weight:700;color:var(--blue);margin-top:14px}
.feature p{font-size:11px;line-height:1.6;color:var(--muted);margin-top:4px}

/* banner */
.banner{position:absolute;left:0;top:1930px;width:1200px;height:480px;background:linear-gradient(90deg,#f6efe9 0%,#f2b48a 35%,var(--orange) 55%,#ee6330 100%)}
.banner-photo{position:absolute;left:0;top:0;width:620px;height:480px;background:linear-gradient(90deg,rgba(225,228,233,.95),rgba(240,180,140,.6) 70%,rgba(242,112,58,0))}
.banner-copy{position:absolute;left:640px;top:150px;width:480px;color:#fff}
.banner-copy h2{font:700 30px/1.2 "Montserrat",sans-serif}
.banner-copy p{font-size:13px;line-height:1.55;margin:14px 0 22px}
.banner-copy .btn{padding:8px 16px;font-size:11px;margin-right:12px}

/* customers */
.customers{position:absolute;left:0;top:2460px;width:1200px;height:680px}
.customers .section-title{margin-top:30px}
.card{position:absolute;top:200px;width:400px;height:340px;background:#fff;box-shadow:0 8px 26px rgba(20,30,60,.12);text-align:center;padding:145px 36px 0}
.card-photo{position:absolute;left:100px;top:-60px;width:190px;height:190px;background:linear-gradient(160deg,#d9dee6,#8e9bb0)}
.card-frame{position:absolute;left:90px;top:-72px;width:190px;height:190px;border:2px solid var(--orange)}
.card h4{font:700 16px "Montserrat",sans-serif;color:var(--blue);margin-top:12px}
.card .role{font-size:12px;color:var(--orange);margin:4px 0 14px}
.card p{font-size:11px;line-height:1.6;color:var(--muted)}
.arrow{position:absolute;top:395px}
.dots{position:absolute;top:610px;left:560px;display:flex;gap:12px}
.dots span{width:9px;height:9px;border-radius:50%;background:#c7ccd4}
.dots span.on{background:var(--orange)}

/* footer */
.site-footer{position:absolute;left:0;top:3150px;width:1200px;height:390px;background:var(--black);color:#d9d9d9}
.footer-brand{position:absolute;left:140px;top:60px;width:280px}
.footer-brand p{font-size:11.5px;line-height:1.6;margin:18px 0 22px;color:#bdbdbd}
.subscribe{display:flex;width:260px;height:36px}
.subscribe span{flex:1;background:#fff;color:#999;font-size:11px;padding:10px 12px}
.subscribe b{width:36px;background:var(--orange);display:flex;align-items:center;justify-content:center}
.footer-col{position:absolute;top:70px}
.footer-col h4{font:700 18px "Montserrat",sans-serif;color:#fff;margin-bottom:20px}
.footer-col li{list-style:none;font-size:11px;margin-bottom:12px;display:flex;align-items:center;gap:10px}
.footer-col li::before{content:"";width:4px;height:4px;background:var(--orange);border-radius:50%}
.footer-col.contact li::before{display:none}
.copyright{position:absolute;left:0;bottom:0;width:1200px;height:36px;border-top:1px solid #2a2a2a;text-align:center;font-size:10px;line-height:36px;color:#8b8b8b}
</style>
</head>
<body>

<section class="hero">
  <header class="site-header">
    <div class="brand">tellvera<span class="brand-dot"></span></div>
    <nav class="nav"><span>CRM</span><span>LOW - CODE</span><span>CUSTOMERS</span><span>RESOURCES</span><span>ABOUT</span></nav>
    <div class="header-tools">
      <span class="lang">ENG ▾</span>
      <span class="search"><svg width="14" height="14" viewBox="0 0 14 14"><circle cx="6" cy="6" r="4.3" fill="none" stroke="#fff" stroke-width="1.6"/><line x1="9.2" y1="9.2" x2="13" y2="13" stroke="#fff" stroke-width="1.6"/></svg></span>
      <span class="btn btn-orange">Talk With Us</span>
    </div>
  </header>
  <div class="hero-copy">
    <h1>UNLEASH BUSINESS<br>VALUE FASTER</h1>
    <p>User friendly and effective solutions for planning, analysis and execution- all gathered in one place.</p>
    <span class="btn btn-orange" style="text-transform:none">Read More →</span>
  </div>
  <div class="hero-visual" role="img" aria-label="Laptop showing business dashboards with bar and pie charts"></div>
</section>

<section class="about">
  <p class="eyebrow">ABOUT TELLVERA</p>
  <h2 class="section-title">TLV VISION AND TLV FOCUS</h2>
  <div class="title-rule"></div>
  <div class="about-frame"></div>
  <div class="about-photo" role="img" aria-label="Business team reviewing printed reports at a desk"></div>
  <div class="about-text">
    <h3>TLV VISION</h3>
    <p>TLV will be the country's leading supplier and competence house on Tellvera software and digital solutions for business management.</p>
    <h3>TLV FOCUS</h3>
    <p>TLV fokuserer på effektiv styring og smarte beslutninger som frigjør tid og ressurser i hele virksomheten. Vi leverer løsninger for planlegging, budsjettering, analyse og oppfølging, samlet i én felles plattform. Gjennom tett samarbeid med kundene utvikler vi verktøy som er enkle å ta i bruk og som gir rask verdi. Våre rådgivere kombinerer dyp bransjeforståelse med teknisk kompetanse innen data og integrasjon. Vi hjelper virksomheter med å automatisere prosesser, forbedre rapportering og styrke beslutningsgrunnlaget. Målet er at hver kunde skal oppnå bedre innsikt, mer kontroll og varig forbedring av sine resultater, uansett størrelse og bransje, både i dag og i årene som kommer fremover.</p>
  </div>
</section>

<section class="platform">
  <h2 class="section-title">TELLVERA PLATFORM</h2>
  <div class="title-rule"></div>
  <p class="platform-sub">A flexible platform that is customised according to your business needs</p>

  <div class="feature" style="left:130px">
    <svg width="70" height="76" viewBox="0 0 70 76"><polygon points="35,2 67,20 67,56 35,74 3,56 3,20" fill="#fff" stroke="#f6c3a8" stroke-width="2"/><circle cx="35" cy="38" r="13" fill="none" stroke="#f2703a" stroke-width="2.5"/><circle cx="35" cy="38" r="4" fill="#f2703a"/></svg>
    <div><h4>PLAN</h4><p>Budgeting &amp; Forecasting ▸</p></div>
  </div>
  <div class="feature" style="left:460px">
    <svg width="70" height="76" viewBox="0 0 70 76"><polygon points="35,2 67,20 67,56 35,74 3,56 3,20" fill="#f2703a"/><rect x="24" y="30" width="22" height="16" fill="none" stroke="#fff" stroke-width="2.5"/><line x1="30" y1="30" x2="30" y2="25" stroke="#fff" stroke-width="2.5"/><line x1="40" y1="30" x2="40" y2="25" stroke="#fff" stroke-width="2.5"/></svg>
    <div><h4>EXECUTE</h4><p>Consolidation ▸<br>Lean Workflow Manager ▸<br>Custom Solution<br>Application ▸</p></div>
  </div>
  <div class="feature" style="left:790px">
    <svg width="70" height="76" viewBox="0 0 70 76"><polygon points="35,2 67,20 67,56 35,74 3,56 3,20" fill="#fff" stroke="#f6c3a8" stroke-width="2"/><rect x="23" y="40" width="6" height="10" fill="#f2703a"/><rect x="32" y="32" width="6" height="18" fill="#f2703a"/><rect x="41" y="26" width="6" height="24" fill="#f2703a"/></svg>
    <div><h4>ANALYZE</h4><p>Reporting &amp; Dashboard ▸<br>Simulate &amp; Predict ▸<br>Self Service ▸</p></div>
  </div>
</section>

<section class="banner">
  <div class="banner-photo" role="img" aria-label="Hands working on a laptop beside printed financial charts"></div>
  <div class="banner-copy">
    <h2>DIGITAL SOLUTIONS AND DATA-DRIVEN BUSINESS DEVELOPMENT THAT CREATE VALUE.</h2>
    <p>TLV Consulting is a consulting company with cutting-edge expertise in digitalization and data-driven business development.</p>
    <span class="btn btn-white">Contact Us</span><span class="btn btn-outline">Read More</span>
  </div>
</section>

<section class="customers">
  <h2 class="section-title">OUR HAPPY CUSTOMERS</h2>
  <div class="title-rule"></div>

  <svg class="arrow" style="left:140px" width="16" height="26" viewBox="0 0 16 26"><polyline points="13,2 3,13 13,24" fill="none" stroke="#555" stroke-width="2.5"/></svg>
  <svg class="arrow" style="left:1044px" width="16" height="26" viewBox="0 0 16 26"><polyline points="3,2 13,13 3,24" fill="none" stroke="#555" stroke-width="2.5"/></svg>

  <div class="card" style="left:180px">
    <div class="card-frame"></div>
    <div class="card-photo" role="img" aria-label="Portrait photo of a smiling client"></div>
    <h4>CLIENT'S NAME</h4>
    <p class="role">Designation</p>
    <p>Working with the team gave us clear numbers, faster planning cycles and far better insight. The rollout was smooth, the support was excellent and our managers now make decisions with real confidence every single day.</p>
  </div>
  <div class="card" style="left:620px">
    <div class="card-frame"></div>
    <div class="card-photo" role="img" aria-label="Portrait photo of a client in a business suit"></div>
    <h4>CLIENT'S NAME</h4>
    <p class="role">Designation</p>
    <p>The platform replaced our scattered spreadsheets with one reliable system. Reporting that used to take weeks is now ready in hours, and our finance team finally has time to focus on analysis and growth.</p>
  </div>

  <div class="dots"><span></span><span class="on"></span><span></span></div>
</section>

<footer class="site-footer">
  <div class="footer-brand">
    <div class="brand" style="font-size:28px">tellvera<span class="brand-dot"></span></div>
    <p>TLV Consulting is a consulting company with cutting-edge expertise in digitalization and data-driven business development.</p>
    <div class="subscribe"><span>Enter your email</span><b><svg width="14" height="14" viewBox="0 0 14 14"><polygon points="1,7 13,1 9,13 7,8" fill="#fff"/></svg></b></div>
  </div>
  <div class="footer-col" style="left:530px">
    <h4>Quick Links</h4>
    <ul><li>CRM</li><li>LOW - CODE</li><li>CUSTOMERS</li><li>RESOURCES</li><li>ABOUT</li></ul>
  </div>
  <div class="footer-col contact" style="left:800px">
    <h4>Contact Us</h4>
    <ul>
      <li><svg width="14" height="14" viewBox="0 0 14 14"><path d="M3 1h3l1 3-2 1.5a8 8 0 0 0 3.5 3.5L10 7l3 1v3a2 2 0 0 1-2 2A10 10 0 0 1 1 3a2 2 0 0 1 2-2z" fill="#f2703a"/></svg>(02) - 318 - 4470</li>
      <li><svg width="14" height="12" viewBox="0 0 14 12"><rect x="1" y="1" width="12" height="10" fill="none" stroke="#f2703a" stroke-width="1.5"/><polyline points="1,1 7,6 13,1" fill="none" stroke="#f2703a" stroke-width="1.5"/></svg>post@tlv.no</li>
    </ul>
  </div>
  <div class="copyright">© 2024 TELLVERA · All Rights Reserved · www.tlv.no</div>
</footer>

</body>
</html>
```